Business card design needed

I need a business card design for a dog walking, dog minding and dog training business. Please refer to my website for the basic company colours and fonts I'm after. Planning on a double sided card, so all information doesn't need to be on the 'front' side.
Cheers

Industry/Entity Type

Dog Training

Contact Information for Business Card

Meadow Paws - happy hounds
Rua 0498307164
meadowpawsdemo.com.au
-walking
-holiday stays
-onsite care
-training and behavioural consultations

```html
<!DOCTYPE html>
<html lang="en">
<head>
<meta charset="utf-8">
<title>Meadow Paws – Business Card</title>
<link rel="stylesheet" href="https://fonts.googleapis.com/css2?family=Courier+Prime:wght@400;700&display=swap">
<style>
  :root {
    --page-bg: #eceae9;
    --card-light: #f3f1f0;
    --card-mid: #cfcac8;
    --card-dark: #4a4240;
    --accent: #c8653f;
    --ink: #5f5755;
    --rule: #8a817e;
  }
  * { margin: 0; padding: 0; box-sizing: border-box; }
  html, body {
    width: 1200px;
    height: 1095px;
    overflow: hidden;
    background: var(--page-bg);
    font-family: "Courier Prime", "Courier New", monospace;
  }
  .sheet {
    width: 1200px;
    height: 1095px;
    display: flex;
    flex-direction: column;
    align-items: center;
    justify-content: center;
    gap: 28px;
  }
  .card {
    position: relative;
    width: 880px;
    height: 506px;
    overflow: hidden;
    box-shadow: 0 6px 18px rgba(0,0,0,0.18);
  }
  .card-photo {
    position: absolute;
    inset: 0;
    background:
      radial-gradient(ellipse 22% 35% at 50% 62%, rgba(255,255,255,0.85), rgba(255,255,255,0) 70%),
      radial-gradient(ellipse 40% 30% at 8% 95%, rgba(60,52,50,0.85), rgba(60,52,50,0) 70%),
      radial-gradient(ellipse 35% 35% at 92% 78%, rgba(60,52,50,0.8), rgba(60,52,50,0) 70%),
      linear-gradient(180deg, var(--card-light) 0%, #e6e2e0 40%, var(--card-mid) 70%, #8c8280 100%);
  }
  .card-back .card-photo {
    background:
      radial-gradient(ellipse 25% 40% at 35% 40%, rgba(255,255,255,0.8), rgba(255,255,255,0) 70%),
      radial-gradient(ellipse 35% 40% at 5% 90%, rgba(60,52,50,0.85), rgba(60,52,50,0) 70%),
      radial-gradient(ellipse 30% 30% at 70% 95%, rgba(70,62,60,0.7), rgba(70,62,60,0) 70%),
      linear-gradient(180deg, var(--card-light) 0%, #e8e4e2 45%, var(--card-mid) 75%, #918885 100%);
  }

  /* Front */
  .brand {
    position: absolute;
    left: 0;
    right: 0;
    top: 208px;
    text-align: center;
  }
  .brand-name {
    font-size: 62px;
    font-weight: 700;
    color: var(--accent);
    letter-spacing: 2px;
    line-height: 1;
  }
  .brand-tagline {
    margin-top: 6px;
    font-size: 21px;
    color: var(--ink);
    letter-spacing: 7px;
    text-transform: uppercase;
  }
  .web {
    position: absolute;
    left: 0;
    right: 0;
    top: 444px;
    text-align: center;
    font-size: 17px;
    letter-spacing: 4px;
    color: var(--ink);
    text-transform: uppercase;
  }

  /* Back */
  .contact {
    position: absolute;
    right: 84px;
    top: 208px;
    text-align: right;
  }
  .services {
    list-style: none;
    font-size: 22px;
    line-height: 27px;
    letter-spacing: 5px;
    color: var(--ink);
    text-transform: uppercase;
  }
  .rule {
    height: 1px;
    width: 520px;
    margin: 12px 0 10px auto;
    background: var(--rule);
  }
  .phone {
    font-size: 52px;
    letter-spacing: 14px;
    margin-right: -14px;
    color: var(--accent);
    line-height: 1;
  }
  .phone-contact {
    display: none;
  }
</style>
</head>
<body>
  <main class="sheet">
    <section class="card card-front">
      <div class="card-photo" role="img" aria-label="Soft-focus photograph of a white dog in a misty grey setting"></div>
      <div class="brand">
        <div class="brand-name">MEADOW PAWS</div>
        <div class="brand-tagline">Happy Hounds</div>
      </div>
      <div class="web">meadowpawsdemo.com.au</div>
    </section>

    <section class="card card-back">
      <div class="card-photo" role="img" aria-label="Soft-focus photograph of a white dog in a misty grey setting"></div>
      <div class="contact">
        <ul class="services">
          <li>Walking</li>
          <li>Holiday Stays</li>
          <li>Onsite Care</li>
          <li>Training</li>
          <li>Behavioural Consultations</li>
        </ul>
        <div class="rule"></div>
        <div class="phone">0498307164</div>
      </div>
    </section>
  </main>
</body>
</html>
```